Product Label Design

We require 2 labels, with the same look and feel, designed for our range of trucking related products for the transport industry. Our logo has been provided.

In terms of the look and feel, we are after:
- a clean and elegant design to represent our premium range of products. By clean we mean not "too busy" or cluttered
- masculine as this relates to trucking,
- must convey that our products are cutting-edge and innovative (our competitors' labels are outdated and dull thus we want to stand-out in the world market)

We want you to create a standardised label template for us, which we can use for several products. We will simply change the product description and product code and reprint.

Each product label will have a:
• Product Description
• Product code
• An image or artwork of a truck as all our products are for the transport industry
• Display product Size in bottom right hand corner
Label 1: 20L (180 mm x 180 mm with 5 mm radius on corners )
Label 2: 750ml (A copy of the 750ml bottle die line has been unloaded as a PDF)

You may use text placeholders for the description.

Files Required:
We need the final design as a psd file, as our business uses Photoshop CS6.

REFERENCE:
Attached is an sample label with the features we want (ie product description, product size, and so on). Please DO NOT use or see this as a reference for your design or style we are after. We do not want your creativity to be restricted by this sample.

Target Market(s)

Products for the trucking industry

Industry/Entity Type

Industry

Colors

Designer to choose colors to be used in the design.

Requirements
Must have
• Logo
• • Image of a truck on the label (preferably the truck should be cutting edge and modern to align it with our product)
• • Some type of background
• • Product description
• • Product code
• • Product size on Bottom Right corner
Should not have
• Unnecessary graphics that will clutter the design

```html
<!DOCTYPE html>
<html lang="en">
<head>
<meta charset="utf-8">
<title>Dravlok Freight – Product Label Set</title>
<link href="https://fonts.googleapis.com/css2?family=Montserrat:wght@600;700;800&display=swap" rel="stylesheet">
<style>
  :root {
    --page-white: #ffffff;
    --stage-grey: #e2e2e2;
    --label-black: #1d1d1d;
    --label-charcoal: #2c2c2c;
    --accent-red: #ea1a4b;
    --text-white: #ffffff;
    --brand-dark: #2b2b2b;
    --truck-dark: #1a1a1a;
    --truck-mid: #4a4a4a;
    --truck-light: #8a8a8a;
  }
  * { margin: 0; padding: 0; box-sizing: border-box; }
  html, body { width: 1200px; height: 1000px; overflow: hidden; }
  body {
    position: relative;
    background: var(--stage-grey);
    font-family: "Montserrat", Arial, sans-serif;
  }

  .brand { display: flex; align-items: center; gap: 12px; font-weight: 800; line-height: 1; letter-spacing: 1px; }
  .brand-dot { border-radius: 50%; flex: none; }
  .brand-name span { display: block; }

  .brand-header {
    position: absolute; left: 0; top: 0; width: 1200px; height: 162px;
    background: var(--page-white);
    display: flex; align-items: center; justify-content: center;
  }
  .brand-header .brand { color: var(--brand-dark); font-size: 56px; gap: 16px; }
  .brand-header .brand-dot { width: 56px; height: 56px; background: var(--brand-dark); }

  .label-square {
    position: absolute; left: 60px; top: 241px; width: 586px; height: 586px;
    border-radius: 14px; overflow: hidden;
    background: radial-gradient(circle at 55% 40%, var(--label-charcoal), var(--label-black) 75%);
    box-shadow: 0 28px 30px -18px rgba(0,0,0,.45);
  }
  .corner-circle {
    position: absolute; left: -95px; top: -95px; width: 190px; height: 190px;
    border-radius: 50%; background: var(--accent-red);
  }
  .size-circle {
    position: absolute; left: 415px; top: 420px; width: 330px; height: 330px;
    border-radius: 50%; background: var(--accent-red);
  }
  .label-square .brand { position: absolute; right: 12px; top: 40px; color: var(--text-white); font-size: 44px; }
  .label-square .brand-dot { width: 40px; height: 40px; background: var(--text-white); }

  .product-info { position: absolute; color: var(--text-white); font-weight: 700; line-height: 1.32; white-space: nowrap; }
  .product-code { color: var(--accent-red); }
  .label-square .product-info { left: 80px; top: 188px; font-size: 47px; letter-spacing: 2.5px; }

  .truck-photo {
    position: absolute;
    background: radial-gradient(ellipse at 55% 45%, var(--truck-light), var(--truck-mid) 40%, var(--truck-dark) 75%);
    border-radius: 18px 18px 10px 10px;
  }
  .label-square .truck-photo { left: 32px; top: 350px; width: 385px; height: 210px; }

  .size-text { position: absolute; color: var(--text-white); font-weight: 700; white-space: nowrap; }
  .label-square .size-text { left: 448px; top: 482px; font-size: 62px; }

  .label-bottle { position: absolute; left: 690px; top: 330px; width: 447px; height: 497px; }
  .label-bottle svg { position: absolute; left: 0; top: 0; filter: drop-shadow(0 14px 12px rgba(0,0,0,.3)); }
  .label-bottle .brand { position: absolute; left: 100px; top: 60px; color: var(--text-white); font-size: 38px; gap: 10px; }
  .label-bottle .brand-dot { width: 34px; height: 34px; background: var(--text-white); }
  .label-bottle .product-info { left: 100px; top: 207px; font-size: 25px; letter-spacing: 2px; line-height: 1.4; }
  .label-bottle .truck-photo { left: 12px; top: 328px; width: 280px; height: 152px; }
  .label-bottle .size-text { left: 302px; top: 440px; font-size: 38px; }
</style>
</head>
<body>
  <header class="brand-header">
    <div class="brand"><span class="brand-dot"></span><div class="brand-name"><span>DRAVLOK</span><span>FREIGHT</span></div></div>
  </header>

  <section class="label-square" aria-label="20 litre label">
    <div class="corner-circle"></div>
    <div class="size-circle"></div>
    <div class="brand"><span class="brand-dot"></span><div class="brand-name"><span>DRAVLOK</span><span>FREIGHT</span></div></div>
    <div class="product-info">
      <p>PRODUCT NAME</p>
      <p>CODE <span class="product-code">20134X</span></p>
    </div>
    <div class="truck-photo" role="img" aria-label="Photo of a black heavy-duty pickup truck, front three-quarter view"></div>
    <p class="size-text">20L</p>
  </section>

  <section class="label-bottle" aria-label="750 millilitre label">
    <svg width="447" height="497" viewBox="0 0 447 497">
      <defs>
        <radialGradient id="bottle-bg" cx="55%" cy="40%" r="70%">
          <stop offset="0" stop-color="#2c2c2c"/>
          <stop offset="1" stop-color="#1d1d1d"/>
        </radialGradient>
        <clipPath id="bottle-shape">
          <path d="M0 200 C0 60 110 0 223.5 0 C337 0 447 60 447 200 L447 485 Q447 497 435 497 L12 497 Q0 497 0 485 Z"/>
        </clipPath>
      </defs>
      <g clip-path="url(#bottle-shape)">
        <rect width="447" height="497" fill="url(#bottle-bg)"/>
        <polygon points="245,497 300,418 447,418 447,497" fill="#ea1a4b"/>
      </g>
    </svg>
    <div class="brand"><span class="brand-dot"></span><div class="brand-name"><span>DRAVLOK</span><span>FREIGHT</span></div></div>
    <div class="product-info">
      <p>PRODUCT NAME</p>
      <p>CODE <span class="product-code">20134X</span></p>
    </div>
    <div class="truck-photo" role="img" aria-label="Photo of a black heavy-duty pickup truck, front three-quarter view"></div>
    <p class="size-text">750ml</p>
  </section>
</body>
</html>
```